Post card

I want an educational customer postcard with our logo, email, and contact number. We are a residential foundation inspection & repair company here in Los Angeles. We provide foundation repair, earthquake retrofitting, and reinforcement.
Our number is 323-555-0148.
Email info@bramblecrestworks.com
Our license number is #2839165

OUR GOAL
Our primary objective is to empower clients with comprehensive knowledge about foundation issues and earthquake retrofitting. By educating them on the potential risks associated with foundation problems and the importance of earthquake retrofitting, we aim to equip homeowners with the necessary information to make informed decisions about safeguarding their properties. Highlighting the benefits of having their houses properly bolted not only enhances structural integrity but also provides peace of mind during seismic events, ensuring the safety and security of their homes and loved ones.

```html
<!DOCTYPE html>
<html lang="en">
<head>
<meta charset="utf-8">
<title>Bramblecrest Works Postcard</title>
<link rel="stylesheet" href="https://fonts.googleapis.com/css2?family=Open+Sans:wght@400;600;700&family=Roboto+Condensed:wght@700&display=swap">
<style>
  :root{
    --page:#e7e8ea;
    --white:#ffffff;
    --navy:#2b4ba0;
    --blue:#2a87cf;
    --blue-light:#6ab9ea;
    --blue-deep:#1f5fb8;
    --red:#d81e26;
    --red-dark:#a8141b;
    --ink:#1d1d1d;
    --line:#8a8a8a;
  }
  *{box-sizing:border-box;margin:0;padding:0}
  html,body{width:1200px;height:642px;overflow:hidden;background:var(--page)}
  body{position:relative;font-family:"Open Sans",sans-serif}
  .card{position:absolute;top:163px;width:392px;height:280px;background:var(--white);overflow:hidden}
  .card--front{left:184px}
  .card--back{left:606px}

  /* shared brand lockup */
  .brand{position:absolute;display:flex;align-items:center;gap:6px}
  .brand__mark{width:20px;height:20px;background:var(--navy);flex:none}
  .brand__name{font-family:"Open Sans",sans-serif;font-weight:700;color:var(--navy);line-height:1.02;letter-spacing:.3px}
  .brand__license{position:absolute;font-size:4px;font-weight:700;color:var(--ink)}

  /* front */
  .front-photo{position:absolute;right:0;top:0;width:250px;height:250px;
    background:linear-gradient(90deg,rgba(255,255,255,0) 0%,rgba(240,183,76,.55) 30%,#e9a43b 55%,#3b4566 100%),
               linear-gradient(180deg,#c7d3e0 0%,#f0c270 60%,#dfe3e8 100%)}
  .front-photo::before{content:"";position:absolute;inset:0;background:linear-gradient(90deg,var(--white) 0%,rgba(255,255,255,0) 35%)}
  .card--front .brand{left:20px;top:20px}
  .card--front .brand__name{font-size:13px;width:110px}
  .card--front .brand__license{left:118px;top:50px}
  .headline-band{position:absolute;left:0;top:71px;width:392px;height:29px;background:var(--navy)}
  .headline{position:absolute;left:14px;top:76px;font-family:"Roboto Condensed",sans-serif;font-weight:700;font-size:15.5px;color:var(--white);letter-spacing:.1px}
  .license-box{position:absolute;left:253px;top:62px;width:89px;height:47px;background:var(--red);color:var(--white);text-align:center;padding-top:6px;font-size:13px;line-height:1.15;letter-spacing:.5px}
  .ribbon{position:absolute;left:29px;top:96px;width:128px;height:21px;background:var(--red);border-radius:0 0 4px 4px;box-shadow:0 2px 3px rgba(0,0,0,.25);
    font-family:"Roboto Condensed",sans-serif;font-weight:700;color:var(--white);font-size:12.5px;text-align:center;line-height:21px}
  .intro{position:absolute;left:19px;top:142px;font-size:11.6px;line-height:16.5px;color:var(--ink);text-transform:uppercase}
  .intro strong{color:var(--red);font-weight:700}
  .footer-band{position:absolute;left:0;top:248px;width:392px;height:32px;background:linear-gradient(180deg,var(--blue-deep),var(--navy))}
  .teeth{position:absolute;left:0;width:392px;height:6px}
  .contact-tab{position:absolute;left:0;top:232px;width:143px;height:48px;background:linear-gradient(90deg,var(--red),var(--red-dark));clip-path:polygon(0 0,100% 0,86% 100%,0 100%);color:var(--white);padding:7px 0 0 20px}
  .contact-tab__lead{font-size:13px;line-height:15px}
  .contact-tab__phone{font-size:13px;font-weight:700;letter-spacing:.4px;line-height:18px}
  .email{position:absolute;right:22px;top:255px;display:flex;align-items:center;gap:5px;color:var(--white);font-size:10px;white-space:nowrap}

  /* back */
  .back-panel{position:absolute;left:0;top:0;width:219px;height:280px;background:linear-gradient(180deg,var(--blue) 0%,var(--blue) 55%,var(--blue-light) 100%)}
  .back-panel__footer{position:absolute;left:0;top:258px;width:219px;height:22px;background:var(--blue-deep)}
  .services{position:absolute;left:18px;top:16px;list-style:none;font-family:"Roboto Condensed",sans-serif;font-weight:700;font-size:10.5px;color:var(--white);line-height:13px}
  .services li{display:flex;align-items:center;gap:4px}
  .services li::before{content:"";width:7px;height:7px;border-radius:50%;background:var(--red)}
  .goal{position:absolute;left:18px;top:64px;width:183px;color:var(--white);font-size:6.2px;line-height:7.7px;text-align:justify}
  .goal p+p{margin-top:6px}
  .work-photo{position:absolute;left:19px;top:178px;width:182px;height:70px;background:linear-gradient(90deg,#c47f64 0%,#b3937f 45%,#3d6b7a 75%,#d9d2c8 100%)}
  .side-tab{position:absolute;left:214px;top:20px;width:36px;height:82px;background:var(--red);display:flex;align-items:center;justify-content:center}
  .side-tab span{transform:rotate(-90deg);white-space:nowrap;font-family:"Roboto Condensed",sans-serif;font-weight:700;color:var(--white);font-size:12px;line-height:12px;text-align:center}
  .stamp{position:absolute;left:326px;top:14px;width:47px;height:50px;border:1px solid #555;border-radius:4px}
  .card--back .brand{left:250px;top:112px}
  .card--back .brand__name{font-size:11px;width:100px}
  .card--back .brand__license{left:325px;top:144px}
  .address{position:absolute;left:235px;top:179px;width:138px;height:79px;border:1px solid #cfcfcf;border-radius:6px;box-shadow:0 1px 3px rgba(0,0,0,.2);padding:4px 7px 0}
  .address span{display:block;border-bottom:.6px solid var(--line);height:17px}
</style>
</head>
<body>

<section class="card card--front" aria-label="Postcard front">
  <div class="front-photo" role="img" aria-label="Photo of a yellow model house with a dark tiled roof"></div>
  <div class="brand">
    <span class="brand__mark"></span>
    <span class="brand__name">BRAMBLECREST WORKS</span>
  </div>
  <span class="brand__license">#2839165</span>
  <div class="headline-band"></div>
  <h1 class="headline">Ensuring the Safety and Security</h1>
  <div class="license-box">LICENSE<br>#2839165</div>
  <div class="ribbon">INSPECTION &amp; REPAIR</div>
  <p class="intro">We are a <strong>residential<br>foundation inspection</strong><br>&amp; repair company here<br>in Los Angeles.</p>
  <div class="footer-band"></div>
  <svg class="teeth" style="top:243px" viewBox="0 0 392 6" preserveAspectRatio="none" aria-hidden="true">
    <path fill="#2b4ba0" d="M0 6 V3 l4 3 4-3 4 3 4-3 4 3 4-3 4 3 4-3 4 3 4-3 4 3 4-3 4 3 4-3 4 3 4-3 4 3 4-3 4 3 4-3 4 3 4-3 4 3 4-3 4 3 4-3 4 3 4-3 4 3 4-3 4 3 4-3 4 3 4-3 4 3 4-3 4 3 4-3 4 3 4-3 4 3 4-3 4 3 4-3 4 3 4-3 4 3 4-3 4 3 4-3 4 3 4-3 4 3 4-3 4 3 4-3 4 3 4-3 4 3 4-3 4 3 4-3 4 3 4-3 4 3 4-3 4 3 4-3 4 3 4-3 4 3 4-3 4 3 4-3 4 3 4-3 4 3 4-3 4 3 4-3 4 3 4-3 4 3 4-3 4 3 4-3 4 3 4-3 4 3 4-3 4 3 4-3 4 3 4-3 4 3 4-3 4 3 4-3 4 3 4-3 4 3 4-3 4 3 4-3 4 3 4-3 4 3 4-3 4 3 4-3 4 3 4-3 4 3 4-3 4 3 4-3 4 3 V6Z"/>
  </svg>
  <div class="contact-tab">
    <p class="contact-tab__lead">Contact Us Today.</p>
    <p class="contact-tab__phone">323-555-0148</p>
  </div>
  <div class="email">
    <svg width="17" height="12" viewBox="0 0 17 12" aria-hidden="true"><rect x="1" y="1" width="15" height="10" fill="#fff" stroke="#d81e26"/><path d="M1 1 L8.5 7 L16 1 M1 11 L6.5 5.5 M16 11 L10.5 5.5" fill="none" stroke="#d81e26"/></svg>
    <span>info@bramblecrestworks.com</span>
  </div>
</section>

<section class="card card--back" aria-label="Postcard back">
  <div class="back-panel"></div>
  <div class="back-panel__footer"></div>
  <svg class="teeth" style="top:253px;width:219px" viewBox="0 0 219 6" preserveAspectRatio="none" aria-hidden="true">
    <path fill="#1f5fb8" d="M0 6 V3 l4 3 4-3 4 3 4-3 4 3 4-3 4 3 4-3 4 3 4-3 4 3 4-3 4 3 4-3 4 3 4-3 4 3 4-3 4 3 4-3 4 3 4-3 4 3 4-3 4 3 4-3 4 3 4-3 4 3 4-3 4 3 4-3 4 3 4-3 4 3 4-3 4 3 4-3 4 3 4-3 4 3 4-3 4 3 4-3 4 3 4-3 4 3 4-3 4 3 4-3 4 3 4-3 4 3 4-3 4 3 4-3 3 3 V6Z"/>
  </svg>
  <ul class="services">
    <li>FOUNDATION REPAIR</li>
    <li>EARTHQUAKE RETROFITTING</li>
    <li>REINFORCEMENT</li>
  </ul>
  <div class="goal">
    <p>Our primary objective is to empower clients with comprehensive knowledge about foundation issues and earthquake retrofitting.</p>
    <p>By educating them on the potential risks associated with foundation problems and the importance of earthquake retrofitting, we aim to equip homeowners with the necessary information to make informed decisions about safeguarding their properties.</p>
    <p>Highlighting the benefits of having their houses properly bolted not only enhances structural integrity but also provides peace of mind during seismic events, ensuring the safety and security of their homes and loved ones.</p>
  </div>
  <div class="work-photo" role="img" aria-label="Photo of a worker in a hard hat cutting a brick wall with an angle grinder"></div>
  <div class="side-tab"><span>INSPECTION<br>&amp; REPAIR</span></div>
  <div class="stamp"></div>
  <div class="brand">
    <span class="brand__mark"></span>
    <span class="brand__name">BRAMBLECREST WORKS</span>
  </div>
  <span class="brand__license">#2839165</span>
  <div class="address"><span></span><span></span><span></span><span></span></div>
</section>

</body>
</html>
```